Accommodation in an Executive Apartment for rent could be a Bed and breakfast,

Currently have a website and like the overall look but it needs revamping and want to add an instant booking button, which I would do later as the unit has a channel manager. Also want to be able to post blogs, etc. Need it to be viewed well on smart phones/tablets. all information related to this unit is on the current site which is www.lorvenstaysmirrabrook.com.au if you would view websites similar to staywell.example and roamtrip.example Must be able to be coded in Wordpress

The current design is done in Wordpress so would want this functionality in any new design.

Target Market(s)

Workers at Quorran precinct, Canberra. Workers at Halvern centre Deakin, Workers at Marlow Peter Tenby Hospital, Workers at Brindlewood Hospital, Public Servants Woden, Workers in Deakin ACT

Industry/Entity Type

Accommodation

Number of Pages Required

5+ page

Font styles to use
Sans Serif

Colors
ec1f27

Requirements
Must have
• Must have a classy look about it. Less clicks through the better. Not to wordy. Hard hitting points,
Nice to have
• Would like to retain the same colour theme and look
Should not have
• anything tacky

```html
<!DOCTYPE html>
<html lang="en">
<head>
<meta charset="utf-8">
<title>Mirrabrook Executive Bed &amp; Breakfast – Facility</title>
<link href="https://fonts.googleapis.com/css2?family=Arimo:wght@400&family=Open+Sans:wght@400;600&display=swap" rel="stylesheet">
<style>
:root{
  --brand-red:#d63b25;
  --brand-red-dark:#b52418;
  --brand-red-light:#e2482c;
  --nav-top:#f4ecd6;
  --nav-bottom:#e6dbbb;
  --nav-line:#c9bd98;
  --nav-text:#3a3a3a;
  --page-bg:#f8f8f6;
  --links-bg:#f1f0ec;
  --text:#1c1c1c;
  --footer-bg:#1f1f1f;
  --footer-text:#e6e6e6;
  --white:#ffffff;
}
*{box-sizing:border-box;margin:0;padding:0}
html,body{width:992px;height:1200px;overflow:hidden}
body{background:var(--page-bg);font-family:"Arimo",Arial,sans-serif;color:var(--text);position:relative}

.site-header{height:115px;background:radial-gradient(ellipse at 50% 40%,var(--brand-red-light) 0%,var(--brand-red) 45%,var(--brand-red-dark) 100%);display:flex;align-items:center;justify-content:center}
.brand-name{font-family:"Open Sans",sans-serif;font-weight:600;font-size:24px;color:var(--white);letter-spacing:.5px}

.main-nav{height:49px;background:linear-gradient(var(--nav-top),var(--nav-bottom));border-bottom:2px solid var(--nav-line);position:relative}
.main-nav a{position:absolute;top:17px;font-family:"Open Sans",sans-serif;font-size:13.5px;letter-spacing:1.3px;color:var(--nav-text);text-decoration:none}
.main-nav a.is-current{color:var(--brand-red)}

.facility-intro{height:433px;padding:43px 97px 0 98px}
.facility-intro p{font-size:15px;line-height:26.5px;margin-bottom:26px;text-align:justify}

.useful-links{position:absolute;top:597px;left:0;width:992px;height:565px;background:var(--links-bg)}
.section-pill{position:absolute;top:-18px;left:391px;width:211px;height:38px;border-radius:19px;background:var(--brand-red);box-shadow:0 2px 3px rgba(0,0,0,.15);color:var(--white);font-family:"Open Sans",sans-serif;font-size:16px;letter-spacing:1.2px;display:flex;align-items:center;justify-content:center}
.link-group{position:absolute;font-size:13.5px;line-height:24px}
.link-group h2{font-weight:400;font-size:16px;text-decoration:underline;text-underline-offset:4px;letter-spacing:.3px;margin-bottom:22px;line-height:20px}
.transport{top:88px;left:98px}
.contacts{top:88px;left:675px}
.info-sites{top:332px;left:677px}

.site-footer{position:absolute;left:0;top:1162px;width:992px;height:38px;background:var(--footer-bg);color:var(--footer-text);font-size:13.5px;display:flex;align-items:center}
.site-footer span{position:absolute}
</style>
</head>
<body>
<header class="site-header">
  <span class="brand-name">Mirrabrook Executive</span>
</header>

<nav class="main-nav">
  <a href="#" style="left:97px">HOME</a>
  <a href="#" class="is-current" style="left:263px">FACILITY</a>
  <a href="#" style="left:465px">NEARBY</a>
  <a href="#" style="left:660px">GALLERY</a>
  <a href="#" style="left:824px">CONTACT</a>
</nav>

<main>
  <section class="facility-intro">
    <p>Situated in the centrally located suburb of Deakin this recently renovated Bed &amp; Breakfast features a separate bedroom and a spacious living area and private access to a kitchen for self catering and also private access to laundry facilities.</p>
    <p>Continental breakfast is supplied, or if preferred supplies for a cooked breakfast can also be provided.</p>
    <p>Deakin is a prestige residential suburb which hosts The Lodge, The Heritage Coin Works and a number of embassies. Being located on the slopes of Red Hill the apartment has pleasant views and offers picturesque walking trails in and around Red Hill. Parliament House is about 2 kilometres distance and the City Centre, Woden Centre and the café precents of Manuka and Kingston are all within a 5 to 10 min drive. The Lakeshore Sailing Club is located in the adjoining lakeside suburb of Yarralumla which is home to a variety of restaurants and boutique shops. It is located within an easy five minute walk of public transport, and is ten minutes from the city, three minutes from Peter Tenby hospital and ten minutes from the Brindlewood hospital.</p>
  </section>

  <section class="useful-links">
    <div class="section-pill">USEFUL LINK</div>

    <div class="link-group transport">
      <h2>TRANSPORT</h2>
      <p>- Capital Connect 13 00 00<br>
      for information on the ACT’s parks and open space system<br>
      - http://livecapitalcity.example<br>
      for more information on living and working in Canberra<br>
      - http://cityservices.example<br>
      for more detail on the information in this guide including bookings, brochures etc.<br>
      - http://capitalareaguide.example<br>
      for self guided walking and drive tours of the Central National Area and more<br>
      information on places of national significance.<br>
      - http://cyclecircle.example<br>
      for bike trails<br>
      - http://cityplanning.example<br>
      for the cycle map and more informationon planning Canberra<br>
      - http://longtrail.example<br>
      for the Heritage Long Trail</p>
    </div>

    <div class="link-group contacts">
      <h2>USEFUL CONTACTS</h2>
      <p>&nbsp;- Metro Link Buses<br>
      &nbsp;- Capital City Cabs<br>
      &nbsp;- Regional Rail<br>
      &nbsp;(Canberra Railway Station)<br>
      &nbsp;- Skyfare Flight Discounts<br>
      &nbsp;- Spindle bicycle hire</p>
    </div>

    <div class="link-group info-sites">
      <h2>INFORMATION SITE</h2>
      <p>- Visit the Capital<br>
      - Capital National University<br>
      - Local weather forecast<br>
      - Capital Events<br>
      - The Story of the Capital</p>
    </div>
  </section>
</main>

<footer class="site-footer">
  <span style="left:69px">Copyright © 2015</span>
  <span style="left:211px">Mirrabrook Executive Bed and Breakfast | Entries (RSS) and Comments (RSS)</span>
  <span style="left:806px">powered by</span>
</footer>
</body>
</html>
```